International online gaming platform needs a game UI design

1. We need a game interface for three kinds of theme based on our guideline and sample mockup.
2. The product type is the online casino games related, we need a series of casino games UIs, however, we can start on the game lobby first.
3. Three theme you might choose from or refer to:
A. 3D look & feel
B. Realistic casino theme
C. Richness and grandeur
D. European casino style
4. NOT ALLOWED to change the design layout.
MUST follow our sample mock up and ONLY redefine the design style.
5. All items must be in a stand-alone component, eg. Button, Tab, Icon,... etc.
6. We need the layout in vector shape, but we can review in JPG or PNG format.
7. The image size: 1366 x 768

Updated:
1. All items and their positions should be same as the sample UI we provided.
Please redesign all the items and create a new theme for it.
No need to create a new layout.
2. Although we accept the draft design, but all the items in UI should be completed.
3. All the wordings in the sample UI are confirmed, you might change the fonts.
4. For the avatar in the left hand side, you don't have to redraw it.
We already have our own avatar system implemented.
5. All the items such as icons, tabs, and buttons are free to redesign.

Dear designers,

We've increased our budget and raise the prize money to 800 USD.  
We also accept the draft design in PNG format and we can go through the details in handover stage.
Thank you very much. 

Reason: Dear designers, We decided to extend the deadline by 7 days. As mentioned in the task description, we are looking for a new style of design and you might refer to the below style. A. 3D look & feel B. Realistic casino theme C. Richness and grandeur D. European casino style If you are still interested in our project, please send us your work. Thank you very much!

Casino

```html
<!DOCTYPE html>
<html lang="en">
<head>
<meta charset="utf-8">
<title>Crestline Live Lobby</title>
<link rel="stylesheet" href="https://fonts.googleapis.com/css2?family=Roboto:wght@400;500;700&display=swap">
<style>
:root{
  --bg-deep:#0f3a86;
  --bg-mid:#2a63c4;
  --bg-light:#5c9be0;
  --panel:#05070d;
  --panel-edge:#1f5fc2;
  --chrome-hi:#f4f6f8;
  --chrome-lo:#8d949c;
  --tab-blue-hi:#6f8fd6;
  --tab-blue-lo:#1f3376;
  --tab-green-hi:#8fe07a;
  --tab-green-lo:#1f7a26;
  --gold:#f2c53c;
  --text-light:#ffffff;
  --text-dark:#1b1b1b;
  --yellow:#f4e321;
  --grid-cell:#ffffff;
  --grid-line:#b8c8dc;
}
*{box-sizing:border-box;margin:0;padding:0}
html,body{width:1200px;height:675px;overflow:hidden}
body{font-family:"Roboto",Arial,sans-serif;color:var(--text-light);background:var(--bg-deep)}
.lobby{position:relative;width:1200px;height:675px;overflow:hidden;
  background:radial-gradient(ellipse at 45% 55%,var(--bg-light) 0%,var(--bg-mid) 40%,var(--bg-deep) 100%)}
.abs{position:absolute}

/* header */
.brand{left:4px;top:4px;width:337px;height:31px;background:var(--panel);border:2px solid #6d6d6d;display:flex;align-items:center;padding-left:12px}
.brand-name{font-family:"Roboto",Arial,sans-serif;font-weight:500;font-size:20px;color:var(--text-light);letter-spacing:.5px}
.clock{left:18px;top:42px;width:165px;height:28px;border-radius:6px;background:linear-gradient(#3b3b3b,#0b0b0b);border:2px solid #555;font-size:10px;display:flex;align-items:center;justify-content:center}
.tool-icons{right:8px;top:5px;display:flex;gap:6px}
.tool{width:33px;height:33px;border:2px solid #fff;border-radius:3px;background:linear-gradient(#4aa0ff,#0a52c8);display:flex;align-items:center;justify-content:center}
.tool.close{background:linear-gradient(#ff6a5a,#c81a10)}

/* game tabs */
.game-tab{top:46px;height:38px;border-radius:19px;border:3px solid #b9c0c8;display:flex;align-items:center;justify-content:center;font-size:21px;font-weight:500;padding-left:40px}
.tab-blue{background:linear-gradient(var(--tab-blue-hi),var(--tab-blue-lo))}
.tab-green{background:linear-gradient(var(--tab-green-hi),var(--tab-green-lo))}
.tab-art{position:absolute;left:-4px;top:-8px;width:56px;height:50px;border-radius:50%}
.art-cards{background:radial-gradient(#ffffff,#9aa3ad)}
.art-six{background:radial-gradient(#f5d35a,#c0392b)}
.art-wheel{background:radial-gradient(#e8c35a 20%,#7a1a12 60%,#c0392b)}
.art-dice{background:radial-gradient(#d93a2c,#3a3e48)}

/* profile */
.profile-panel{left:13px;top:79px;width:183px;height:272px;border-radius:10px;background:var(--panel);border:3px solid var(--panel-edge)}
.avatar{position:absolute;left:10px;top:15px;width:157px;height:183px;border:3px solid #777;background:linear-gradient(#3a3a3a,#0e0e0e 70%)}
.avatar-fill{position:absolute;left:20px;top:20px;right:20px;bottom:0;border-radius:50% 50% 8px 8px;background:linear-gradient(#c99a78,#6a7078 60%,#3d6ea0)}
.player-name{position:absolute;left:10px;top:198px;width:157px;height:22px;background:linear-gradient(#7b7b7b,#3e3e3e);font-size:15px;display:flex;align-items:center;justify-content:center}
.profile-btn{position:absolute;left:8px;top:226px;width:161px;height:32px;border-radius:4px;background:linear-gradient(#3f82ee,#1247b0);font-size:16px;display:flex;align-items:center;gap:18px;padding-left:6px}
.doc-icon{width:22px;height:22px;background:#111;border:1px solid #555;border-radius:2px}

.menu-panel{left:13px;top:369px;width:183px;height:255px;border-radius:10px;background:var(--panel);border:3px solid var(--panel-edge)}
.menu-btn{position:absolute;left:8px;width:150px;height:31px;border-radius:6px;border:2px solid #9bb8ea;background:linear-gradient(#3a78e0,#123f9a);font-size:11.5px;display:flex;align-items:center;gap:8px;padding-left:4px}
.menu-ico{width:22px;height:22px;border-radius:3px;background:linear-gradient(#6aaaf5,#1f5fc2);border:1px solid #fff;display:flex;align-items:center;justify-content:center}

/* dealers */
.dealer-main{left:211px;top:97px;width:264px;height:125px;border-radius:4px;background:linear-gradient(#e6e8ea,#8a9097);padding:7px}
.dealer-row{left:496px;top:97px;width:686px;height:118px;background:linear-gradient(#e6e8ea,#8a9097);border-radius:4px;padding:10px 12px;display:flex;gap:12px}
.dealer-card{position:relative;background:#000;border:2px solid #555;border-radius:3px}
.dealer-card.main{width:250px;height:111px}
.dealer-card.small{width:212px;height:90px}
.dealer-photo{position:absolute;left:3px;top:3px;border-radius:6px;border:2px solid #2e8bf0;background:linear-gradient(#4a6f96,#0b1420)}
.main .dealer-photo{width:84px;height:80px}
.small .dealer-photo{width:68px;height:66px}
.road{position:absolute;top:3px;right:3px;background-color:var(--grid-cell);
  background-image:linear-gradient(var(--grid-line) 1px,transparent 1px),linear-gradient(90deg,var(--grid-line) 1px,transparent 1px);background-size:11px 11px}
.main .road{left:90px;height:80px}
.small .road{left:74px;height:66px}
.dealer-bar{position:absolute;left:0;right:0;bottom:0;display:flex;align-items:center;justify-content:space-between;background:#000}
.main .dealer-bar{height:26px;font-size:11px;padding-left:10px}
.small .dealer-bar{height:18px;font-size:8px;padding-left:6px}
.deals{height:100%;background:linear-gradient(#2a6fd0,#123a80);display:flex;align-items:center;padding:0 8px}
.main .deals{width:72px}

/* filter bar */
.filter-bar{left:204px;top:230px;width:980px;height:35px;border-radius:6px;background:#050607;border:2px solid #2c2c2c}
.chip{position:absolute;top:3px;height:27px;border-radius:4px;background:linear-gradient(var(--chrome-hi),var(--chrome-lo));color:var(--text-dark);font-size:11px;display:flex;align-items:center;justify-content:center;gap:4px}
.search{border-radius:14px}
.person-ico{width:26px;height:22px;background:#111;border-radius:3px;display:flex;align-items:center;justify-content:center}

/* tables */
.table-card{width:279px;height:142px;border-radius:6px;border:3px solid #c9ced4;background:linear-gradient(#000 55%,#1e4a16 75%,#000 80%)}
.table-info{position:absolute;left:0;right:0;top:4px;padding:0 8px;font-size:11px;display:flex;justify-content:space-between;line-height:15px}
.table-info .yel{color:var(--yellow)}
.table-info .right{text-align:right}
.table-svg{position:absolute;left:0;top:0}
.seats{position:absolute;left:3px;right:3px;bottom:3px;height:27px;display:flex;gap:2px}
.seat{flex:1;border-radius:2px;background:linear-gradient(#2c8a48,#0e4a22);display:flex;align-items:center;justify-content:center}
.seat.open{background:linear-gradient(#f6cf4a,#a77210)}

.scrollbar{left:1171px;top:300px;width:12px;height:306px;background:#000;border-radius:2px}
.scroll-thumb{position:absolute;left:-2px;top:10px;width:16px;height:24px;border-radius:3px;background:linear-gradient(#fff,#888)}

.balance{left:938px;top:639px;width:252px;height:32px;border-radius:8px;background:linear-gradient(#3a3a3a,#0a0a0a);border:2px solid #555;display:flex;align-items:center;font-size:16px}
.balance-label{width:94px;text-align:center}
.currency{width:42px;height:22px;background:linear-gradient(#c7962e,#5a3a08);border:1px solid #e8c56a;font-size:9px;display:flex;align-items:center;justify-content:center}
.balance-value{flex:1;padding-left:8px;font-size:15px}
.balance-end{width:10px;height:24px;background:var(--gold);border-radius:2px;margin-right:4px}
</style>
</head>
<body>
<svg width="0" height="0" style="position:absolute">
  <defs>
    <radialGradient id="coinGrad" cx="40%" cy="35%" r="70%">
      <stop offset="0" stop-color="#fff3b0"/><stop offset=".5" stop-color="#f2c53c"/><stop offset="1" stop-color="#9a6a0a"/>
    </radialGradient>
    <symbol id="user" viewBox="0 0 20 20"><circle cx="10" cy="6" r="4.5" fill="#f6c9a0"/><path d="M2 19c0-6 4-8 8-8s8 2 8 8z" fill="#f6c9a0"/></symbol>
    <symbol id="down" viewBox="0 0 20 20"><path d="M3 6h14l-7 9z" fill="#6b4306"/></symbol>
    <symbol id="table" viewBox="0 0 279 142">
      <ellipse cx="140" cy="100" rx="138" ry="4" fill="#7fd14a" opacity=".6"/>
      <g stroke="#fff" stroke-width="1" fill="none">
        <path d="M30 55H250L272 100H8Z"/>
        <path d="M20 76H260"/>
        <path d="M61.4 55L45.7 100M92.9 55L83.4 100M124.3 55L121.1 100M155.7 55L158.9 100M187.1 55L196.6 100M218.6 55L234.3 100"/>
      </g>
      <g font-family="Roboto,Arial,sans-serif" font-size="10" font-weight="700" font-style="italic" text-anchor="middle">
        <g fill="#f4e321"><text x="40" y="70">B</text><text x="73" y="70">B</text><text x="106" y="70">B</text><text x="140" y="70">B</text><text x="174" y="70">B</text><text x="207" y="70">B</text><text x="240" y="70">B</text></g>
        <g fill="#fff"><text x="33" y="92">P</text><text x="69" y="92">P</text><text x="104" y="92">P</text><text x="140" y="92">P</text><text x="176" y="92">P</text><text x="211" y="92">P</text><text x="247" y="92">P</text></g>
      </g>
      <circle cx="140" cy="30" r="27" fill="url(#coinGrad)" stroke="#8a5a08" stroke-width="1.5"/>
      <circle cx="140" cy="30" r="21" fill="none" stroke="#c8921c" stroke-width="1"/>
      <text x="140" y="35" text-anchor="middle" font-family="Roboto,Arial,sans-serif" font-size="13" fill="#8a5a08">JOIN</text>
    </symbol>
  </defs>
</svg>

<main class="lobby">
  <div class="lobby-bg abs" role="img" aria-label="Faint playing card suit decoration" style="inset:0;background:radial-gradient(circle at 30% 70%,rgba(255,255,255,.08),transparent 40%),radial-gradient(circle at 75% 30%,rgba(255,255,255,.06),transparent 35%)"></div>

  <header>
    <div class="brand abs"><span class="brand-name">Crestline Live</span></div>
    <div class="clock abs">12/03/2014&nbsp;&nbsp;09 : 18 AM</div>
    <nav class="tool-icons abs">
      <div class="tool" aria-label="Search"><svg width="20" height="20" viewBox="0 0 20 20"><circle cx="8" cy="8" r="5.5" fill="none" stroke="#fff" stroke-width="2.5"/><path d="M12 12l6 6" stroke="#fff" stroke-width="3"/></svg></div>
      <div class="tool" aria-label="Currency"><svg width="20" height="20" viewBox="0 0 20 20"><circle cx="10" cy="10" r="7.5" fill="none" stroke="#fff" stroke-width="2.5"/><text x="10" y="14" text-anchor="middle" font-size="11" font-weight="700" fill="#fff" font-family="Arial,sans-serif">$</text></svg></div>
      <div class="tool" aria-label="Fullscreen"><svg width="20" height="20" viewBox="0 0 20 20" fill="none" stroke="#fff" stroke-width="2.5"><path d="M2 7V2h5M13 2h5v5M18 13v5h-5M7 18H2v-5"/></svg></div>
      <div class="tool" aria-label="Music"><svg width="20" height="20" viewBox="0 0 20 20" fill="#fff"><path d="M7 3h10v3H9v9a3 3 0 1 1-2-2.8z"/><path d="M15 6h2v8a3 3 0 1 1-2-2.8z"/></svg></div>
      <div class="tool close" aria-label="Close"><svg width="20" height="20" viewBox="0 0 20 20" stroke="#fff" stroke-width="3.5"><path d="M3 3l14 14M17 3L3 17"/></svg></div>
    </nav>
  </header>

  <nav class="game-tabs">
    <div class="game-tab tab-blue abs" style="left:202px;width:224px"><span class="tab-art art-cards" role="img" aria-label="Fanned playing cards"></span>Bacarat</div>
    <div class="game-tab tab-green abs" style="left:439px;width:228px"><span class="tab-art art-six" role="img" aria-label="Cards with chips and number six"></span>Super six</div>
    <div class="game-tab tab-green abs" style="left:676px;width:228px"><span class="tab-art art-wheel" role="img" aria-label="Roulette wheel"></span>Roulette</div>
    <div class="game-tab tab-green abs" style="left:918px;width:224px"><span class="tab-art art-dice" role="img" aria-label="Dice cup with dice"></span>Sic Bo</div>
  </nav>

  <aside>
    <section class="profile-panel abs">
      <div class="avatar"><div class="avatar-fill" role="img" aria-label="Player avatar"></div></div>
      <div class="player-name">Ryn208</div>
      <div class="profile-btn"><span class="doc-icon"></span>Profile</div>
    </section>
    <section class="menu-panel abs">
      <div class="menu-btn" style="top:13px"><span class="menu-ico"><svg width="14" height="14" viewBox="0 0 14 14" fill="none" stroke="#fff" stroke-width="2"><circle cx="2.5" cy="11.5" r="1.5" fill="#fff"/><path d="M1 6a7 7 0 0 1 7 7M1 1a12 12 0 0 1 12 12"/></svg></span>Announcements</div>
      <div class="menu-btn" style="top:59px"><span class="menu-ico"><svg width="14" height="14" viewBox="0 0 14 14"><rect x="5.5" y="1" width="3" height="8" fill="#fff"/><rect x="5.5" y="10.5" width="3" height="3" fill="#fff"/></svg></span>Rules &amp; Regulation</div>
      <div class="menu-btn" style="top:106px"><span class="menu-ico"><svg width="14" height="14" viewBox="0 0 14 14" fill="none" stroke="#fff" stroke-width="2"><circle cx="8" cy="6" r="4"/><path d="M5 9l-4 4"/></svg></span>Quick tour</div>
    </section>
  </aside>

  <section class="dealers">
    <div class="dealer-main abs">
      <div class="dealer-card main">
        <div class="dealer-photo" role="img" aria-label="Dealer portrait"></div>
        <div class="road"></div>
        <div class="dealer-bar"><span>Dealer Name</span><span class="deals">Deals 999</span></div>
      </div>
    </div>
    <div class="dealer-row abs">
      <div class="dealer-card small"><div class="dealer-photo" role="img" aria-label="Dealer portrait"></div><div class="road"></div><div class="dealer-bar"><span>Dealer Name</span><span class="deals">Deals 999</span></div></div>
      <div class="dealer-card small"><div class="dealer-photo" role="img" aria-label="Dealer portrait"></div><div class="road"></div><div class="dealer-bar"><span>Dealer Name</span><span class="deals">Deals 999</span></div></div>
      <div class="dealer-card small"><div class="dealer-photo" role="img" aria-label="Dealer portrait"></div><div class="road"></div><div class="dealer-bar"><span>Dealer Name</span><span class="deals">Deals 999</span></div></div>
    </div>
  </section>

  <div class="filter-bar abs">
    <div class="chip" style="left:9px;width:140px;justify-content:flex-start;gap:14px;padding-left:4px"><span class="person-ico"><svg width="14" height="14"><use href="#user" fill="#fff"/></svg></span>Multiplayer</div>
    <div class="chip search" style="left:154px;width:285px"></div>
    <div class="chip" style="left:459px;width:112px">Join any</div>
    <div class="chip" style="left:573px;width:38px;font-size:12px">A→Z</div>
    <div class="chip" style="left:613px;width:38px;font-size:13px;font-weight:700">$↓</div>
    <div class="chip" style="left:655px;width:38px;font-size:13px;font-weight:700">$↑</div>
    <div class="chip" style="left:719px;width:44px"><svg width="26" height="18" viewBox="0 0 26 18"><circle cx="8" cy="5" r="4" fill="#111"/><circle cx="18" cy="5" r="4" fill="#111"/><path d="M1 18c0-6 3-8 7-8s7 2 7 8zM11 18c0-6 3-8 7-8s7 2 7 8z" fill="#111"/></svg></div>
    <div class="chip" style="left:765px;width:42px;font-size:13px">≤ 3</div>
    <div class="chip" style="left:809px;width:42px;font-size:13px">&gt; 3</div>
    <div class="chip" style="left:856px;width:112px;font-size:13px">All Limits <svg width="12" height="8"><path d="M0 0h12L6 8z" fill="#111"/></svg></div>
  </div>

  <section class="tables">
    <article class="table-card abs" style="left:239px;top:303px">
      <svg class="table-svg" width="273" height="136" viewBox="0 0 279 142"><use href="#table"/></svg>
      <div class="table-info"><div><span class="yel">Baccarat A5-3C</span><br>Bet Limit</div><div class="right"><span class="yel">Commission 0/7</span><br>0/100</div></div>
      <div class="seats"><div class="seat"><svg width="18" height="18"><use href="#user"/></svg></div><div class="seat"><svg width="18" height="18"><use href="#user"/></svg></div><div class="seat"><svg width="18" height="18"><use href="#user"/></svg></div><div class="seat"><svg width="18" height="18"><use href="#user"/></svg></div><div class="seat"><svg width="18" height="18"><use href="#user"/></svg></div><div class="seat open"><svg width="18" height="18"><use href="#down"/></svg></div><div class="seat open"><svg width="18" height="18"><use href="#down"/></svg></div></div>
    </article>
    <article class="table-card abs" style="left:549px;top:303px">
      <svg class="table-svg" width="273" height="136" viewBox="0 0 279 142"><use href="#table"/></svg>
      <div class="table-info"><div><span class="yel">Baccarat A5-3C</span><br>Bet Limit</div><div class="right"><span class="yel">Commission 0/7</span><br>0/100</div></div>
      <div class="seats"><div class="seat"><svg width="18" height="18"><use href="#user"/></svg></div><div class="seat"><svg width="18" height="18"><use href="#user"/></svg></div><div class="seat"><svg width="18" height="18"><use href="#user"/></svg></div><div class="seat"><svg width="18" height="18"><use href="#user"/></svg></div><div class="seat"><svg width="18" height="18"><use href="#user"/></svg></div><div class="seat open"><svg width="18" height="18"><use href="#down"/></svg></div><div class="seat open"><svg width="18" height="18"><use href="#down"/></svg></div></div>
    </article>
    <article class="table-card abs" style="left:859px;top:303px">
      <svg class="table-svg" width="273" height="136" viewBox="0 0 279 142"><use href="#table"/></svg>
      <div class="table-info"><div><span class="yel">Baccarat A5-3C</span><br>Bet Limit</div><div class="right"><span class="yel">Commission 0/7</span><br>0/100</div></div>
      <div class="seats"><div class="seat"><svg width="18" height="18"><use href="#user"/></svg></div><div class="seat"><svg width="18" height="18"><use href="#user"/></svg></div><div class="seat"><svg width="18" height="18"><use href="#user"/></svg></div><div class="seat"><svg width="18" height="18"><use href="#user"/></svg></div><div class="seat"><svg width="18" height="18"><use href="#user"/></svg></div><div class="seat open"><svg width="18" height="18"><use href="#down"/></svg></div><div class="seat open"><svg width="18" height="18"><use href="#down"/></svg></div></div>
    </article>
    <article class="table-card abs" style="left:239px;top:464px">
      <svg class="table-svg" width="273" height="136" viewBox="0 0 279 142"><use href="#table"/></svg>
      <div class="table-info"><div><span class="yel">Baccarat A5-3C</span><br>Bet Limit</div><div class="right"><span class="yel">Commission 0/7</span><br>0/100</div></div>
      <div class="seats"><div class="seat"><svg width="18" height="18"><use href="#user"/></svg></div><div class="seat"><svg width="18" height="18"><use href="#user"/></svg></div><div class="seat"><svg width="18" height="18"><use href="#user"/></svg></div><div class="seat"><svg width="18" height="18"><use href="#user"/></svg></div><div class="seat"><svg width="18" height="18"><use href="#user"/></svg></div><div class="seat open"><svg width="18" height="18"><use href="#down"/></svg></div><div class="seat open"><svg width="18" height="18"><use href="#down"/></svg></div></div>
    </article>
    <article class="table-card abs" style="left:549px;top:464px">
      <svg class="table-svg" width="273" height="136" viewBox="0 0 279 142"><use href="#table"/></svg>
      <div class="table-info"><div><span class="yel">Baccarat A5-3C</span><br>Bet Limit</div><div class="right"><span class="yel">Commission 0/7</span><br>0/100</div></div>
      <div class="seats"><div class="seat"><svg width="18" height="18"><use href="#user"/></svg></div><div class="seat"><svg width="18" height="18"><use href="#user"/></svg></div><div class="seat"><svg width="18" height="18"><use href="#user"/></svg></div><div class="seat"><svg width="18" height="18"><use href="#user"/></svg></div><div class="seat"><svg width="18" height="18"><use href="#user"/></svg></div><div class="seat open"><svg width="18" height="18"><use href="#down"/></svg></div><div class="seat open"><svg width="18" height="18"><use href="#down"/></svg></div></div>
    </article>
    <article class="table-card abs" style="left:862px;top:463px">
      <svg class="table-svg" width="273" height="136" viewBox="0 0 279 142"><use href="#table"/></svg>
      <div class="table-info"><div><span class="yel">Baccarat A5-3C</span><br>Bet Limit</div><div class="right"><span class="yel">Commission 0/7</span><br>0/100</div></div>
      <div class="seats"><div class="seat"><svg width="18" height="18"><use href="#user"/></svg></div><div class="seat"><svg width="18" height="18"><use href="#user"/></svg></div><div class="seat"><svg width="18" height="18"><use href="#user"/></svg></div><div class="seat"><svg width="18" height="18"><use href="#user"/></svg></div><div class="seat"><svg width="18" height="18"><use href="#user"/></svg></div><div class="seat open"><svg width="18" height="18"><use href="#down"/></svg></div><div class="seat open"><svg width="18" height="18"><use href="#down"/></svg></div></div>
    </article>
  </section>

  <div class="scrollbar abs"><div class="scroll-thumb"></div></div>

  <footer class="balance abs">
    <span class="balance-label">Balance</span>
    <span class="currency">$ SGD ‹</span>
    <span class="balance-value">999,999,999</span>
    <span class="balance-end"></span>
  </footer>
</main>
</body>
</html>
```